Brix2Key Header

I want a professional Letterhead for my law firm. I'm attaching the letterhead I currently use in Word and PDF form. I'm also attaching my logo, and an example header that I like.

```html
<!DOCTYPE html>
<html lang="en">
<head>
<meta charset="utf-8">
<title>Brix2Key Letterhead</title>
<link href="https://fonts.googleapis.com/css2?family=Open+Sans:wght@400;600;800&display=swap" rel="stylesheet">
<style>
  :root {
    --backdrop: #e4e4e4;
    --paper: #ffffff;
    --ink: #2b2b2b;
    --body-text: #4a4a4a;
    --brand-blue: #1b75bc;
    --brand-green: #3c9a3e;
    --rule: #555555;
    --signature-tone: #d9d9d9;
  }
  * { margin: 0; padding: 0; box-sizing: border-box; }
  html, body {
    width: 1040px; height: 1200px; overflow: hidden;
    background: var(--backdrop);
    font-family: "Open Sans", Arial, sans-serif;
  }
  .letterhead {
    position: absolute; left: 54px; top: 0;
    width: 932px; height: 1200px;
    background: var(--paper);
    color: var(--body-text);
  }
  .side-band { position: absolute; left: 0; top: 0; width: 20px; height: 1200px; }
  .wordmark {
    position: absolute; top: 26px; left: 0; width: 932px;
    text-align: center;
    font-weight: 800; font-size: 46px; line-height: 64px; color: var(--ink);
    letter-spacing: 1px;
  }
  .letter-body { position: absolute; left: 88px; width: 754px; font-size: 14.5px; }
  .issue-date { top: 223px; }
  .recipient { top: 260px; line-height: 18px; }
  .salutation { top: 364px; }
  .paragraph { line-height: 27px; text-align: justify; hyphens: auto; }
  .p1 { top: 403px; }
  .p2 { top: 565px; }
  .p3 { top: 673px; }
  .closing { top: 821px; }
  .signature-mark {
    position: absolute; left: 88px; top: 853px; width: 216px; height: 26px;
    background: var(--signature-tone); border-radius: 3px;
  }
  .signer-name { top: 890px; font-size: 18px; color: var(--ink); font-weight: 600; }
  .signer-title { top: 922px; }
  .footer-address {
    position: absolute; top: 1122px; left: 0; width: 932px;
    text-align: center; font-size: 17px; color: var(--ink);
  }
  .footer-rule {
    position: absolute; top: 1150px; left: 167px; width: 599px;
    border-top: 1px solid var(--rule);
  }
  .footer-contacts {
    position: absolute; top: 1157px; left: 0; width: 932px;
    text-align: center; font-size: 17px; color: var(--ink); white-space: nowrap;
  }
  .footer-contacts .label { color: var(--brand-blue); font-weight: 600; }
  .footer-contacts .sep { margin: 0 8px; }
</style>
</head>
<body>
  <main class="letterhead">
    <svg class="side-band" viewBox="0 0 20 1200" aria-hidden="true">
      <polygon points="0,0 20,0 20,558 0,533" fill="var(--brand-blue)"/>
      <polygon points="0,545 20,570 20,1200 0,1200" fill="var(--brand-green)"/>
    </svg>

    <div class="wordmark">Brix2Key</div>

    <p class="letter-body issue-date">Issuing Date: May 5, 2018</p>
    <p class="letter-body recipient">Name Of Employee Mr. XYZABC<br>Address of Employee<br>Address Line 2 etc..</p>
    <p class="letter-body salutation">Dear Mr.XYZABC</p>

    <p class="letter-body paragraph p1">Lorem Ipsum has been the industry's standard dummy text ever since the 1500s, when an unknown printer took a galley of type and scrambled it to make a type specimen book. It has survived not only five centuries, but also the leap into electronic typesetting, remaining essentially unchanged. It was popularised in the 1960s with the release of Typeleaf sheets containing Lorem Ipsum passages, and more recently with desktop publishing software like Vellum PageCraft including versions of Lorem Ipsum.</p>
    <p class="letter-body paragraph p2">Lorem Ipsum is simply dummy text of the printing and typesetting industry. Lorem Ipsum has been the industry's standard dummy text ever since the 1500s, when an unknown printer took a galley of type and scrambled it to make a type specimen book.</p>
    <p class="letter-body paragraph p3">It has survived not only five centuries, but also the leap into electronic typesetting, remaining essentially unchanged. It was popularised in the 1960s with the release of Typeleaf sheets containing Lorem IpsumIpsum passages.</p>

    <p class="letter-body closing">Yours Sincerely</p>
    <div class="signature-mark" role="img" aria-label="Handwritten signature of Daniel Reyes"></div>
    <p class="letter-body signer-name">Daniel Reyes</p>
    <p class="letter-body signer-title">Managing Director</p>

    <p class="footer-address">1846 Larkspur Ave. Ste 100 Austin, TX 78701</p>
    <div class="footer-rule"></div>
    <p class="footer-contacts">
      <span class="label">P:</span> 877.555.0142<span class="sep">|</span><span class="label">F:</span> 469.555.0187<span class="sep">|</span><span class="label">E:</span> info@brix2key.net<span class="sep">|</span><span class="label">W:</span> brix2key.com
    </p>
  </main>
</body>
</html>
```